new roofing company card

New primary business card for roofing company.

Industry/Entity Type

Residential roofing/Specializing in Asphalt and Standing seam metal roofing

Contact Information for Business Card

Phone number is: 484 672 1058 Email: support@fennridgeroofworks.com website: www.fennridgeroofworks.com

Colors
EB3D1F
EC4F4E
F09395
F8D3D4
FCEDEE

```html
<!DOCTYPE html>
<html lang="en">
<head>
<meta charset="utf-8">
<title>Fennridge Roofworks – Business Card</title>
<link rel="stylesheet" href="https://fonts.googleapis.com/css2?family=Arimo:wght@400;700&display=swap">
<style>
  :root {
    --brand-red: #c23425;
    --brand-red-deep: #a52a1e;
    --accent-red: #d8382a;
    --ink: #1c1c1c;
    --ink-soft: #3d3d3d;
    --divider: #c9c9c9;
    --paper: #ffffff;
    --backdrop: #e9e9e9;
  }
  * { box-sizing: border-box; margin: 0; padding: 0; }
  html, body {
    width: 1200px; height: 874px; overflow: hidden;
    background: var(--backdrop);
    font-family: "Arimo", Arial, sans-serif;
  }
  .canvas {
    width: 1200px; height: 874px;
    display: flex; flex-direction: column;
    align-items: center; justify-content: center; gap: 56px;
  }
  .card {
    width: 600px; height: 343px;
    border-radius: 22px;
    box-shadow: 0 10px 28px rgba(0,0,0,.18);
    position: relative; overflow: hidden;
  }
  /* back */
  .card-back {
    background: var(--brand-red);
    display: flex; align-items: center; justify-content: center;
  }
  .card-back .brand-name {
    color: var(--brand-red-deep);
    font-size: 44px; font-weight: 700; letter-spacing: 1px;
    text-align: center; line-height: 1.1;
  }
  /* front */
  .card-front { background: var(--paper); }
  .brand-block {
    position: absolute; left: 40px; top: 0; bottom: 40px; width: 210px;
    display: flex; flex-direction: column; align-items: center; justify-content: center; gap: 14px;
  }
  .brand-block .brand-square {
    width: 22px; height: 22px; background: var(--accent-red);
  }
  .brand-block .brand-name {
    color: var(--ink);
    font-size: 28px; font-weight: 700; text-align: center; line-height: 1.15;
  }
  .divider {
    position: absolute; left: 278px; top: 92px; height: 135px;
    width: 1px; background: var(--divider);
  }
  .contact-block {
    position: absolute; left: 306px; top: 100px;
  }
  .person-name {
    font-size: 27px; font-weight: 700; color: var(--ink); letter-spacing: .5px;
  }
  .person-title {
    font-size: 15px; color: var(--accent-red); margin-top: 3px;
  }
  .contact-list { list-style: none; margin-top: 22px; }
  .contact-list li {
    display: flex; align-items: center; gap: 10px;
    font-size: 15.5px; color: var(--ink-soft); line-height: 23px;
  }
  .contact-list svg { width: 13px; height: 13px; fill: var(--accent-red); flex: none; }
  .base-rule {
    position: absolute; left: 0; right: 0; bottom: 22px;
    height: 3px; background: var(--accent-red);
  }
  .base-band {
    position: absolute; left: 0; right: 0; bottom: 0;
    height: 14px; background: var(--ink-soft);
  }
</style>
</head>
<body>
<main class="canvas">
  <section class="card card-back">
    <p class="brand-name">FENNRIDGE<br>ROOFWORKS</p>
  </section>

  <section class="card card-front">
    <div class="brand-block">
      <span class="brand-square"></span>
      <p class="brand-name">FENNRIDGE<br>ROOFWORKS</p>
    </div>
    <div class="divider"></div>
    <div class="contact-block">
      <h1 class="person-name">DANIEL MARSH</h1>
      <p class="person-title">President</p>
      <ul class="contact-list">
        <li>
          <svg viewBox="0 0 24 24" aria-hidden="true"><path d="M6.6 10.8a15.1 15.1 0 0 0 6.6 6.6l2.2-2.2a1 1 0 0 1 1-.25 11.4 11.4 0 0 0 3.6.57 1 1 0 0 1 1 1V20a1 1 0 0 1-1 1A17 17 0 0 1 3 4a1 1 0 0 1 1-1h3.5a1 1 0 0 1 1 1c0 1.25.2 2.45.57 3.6a1 1 0 0 1-.25 1z"/></svg>
          484 672 1058
        </li>
        <li>
          <svg viewBox="0 0 24 24" aria-hidden="true"><path d="M2 5h20v14H2z M3.5 6.5 12 13l8.5-6.5" /><path d="M2 5l10 8 10-8v1.8l-10 8-10-8z" fill="#fff"/></svg>
          support@fennridgeroofworks.com
        </li>
        <li>
          <svg viewBox="0 0 24 24" aria-hidden="true"><circle cx="12" cy="12" r="10"/><path d="M2 12h20M12 2c3 3 3 17 0 20M12 2c-3 3-3 17 0 20" stroke="#fff" stroke-width="1.6" fill="none"/></svg>
          www.fennridgeroofworks.com
        </li>
      </ul>
    </div>
    <div class="base-rule"></div>
    <div class="base-band"></div>
  </section>
</main>
</body>
</html>
```